Frost Harbor Supply Inc. Box Truck Wrap

I'm looking for design ideas for wrapping my box truck using any of these photos or ideas you may have. Nothing too colorful but more professional. We are looking to target ice cream shop owners and not children as we are just a delivery truck. Nothing too cartoonish. Please feel free to use any of the photos I have uploaded or if you have a better idea you are welcome to give that a shot.

Target Market(s)

Small business like ice cream shops

Industry/Entity Type

Ice Cream product wholesale distributor

Requirements
Must have
• our logo, phone #: 856-217-6094, website: www.frostharborsupplyinc.example, email: sales@frostharborsupplyinc.example, product categories we carry. (Ice Cream, Mixes, Syrups/Bases, Topping, Cones, Water Ice )
Nice to have
• Pictures of the products
Should not have
• not too colorful. more professional

```html
<!DOCTYPE html>
<html lang="en">
<head>
<meta charset="utf-8">
<title>Frost Harbor Supply Inc. Truck Wrap</title>
<link rel="stylesheet" href="https://fonts.googleapis.com/css2?family=League+Spartan:wght@600&family=Josefin+Sans:wght@400&family=Roboto:wght@400;500&display=swap">
<style>
  :root {
    --paper: #ffffff;
    --band: #b9b5de;
    --slate: #6f6b88;
    --stripe: #aab0dc;
    --ink: #5a45c6;
    --frame: #4b2a9a;
  }
  html, body {
    margin: 0;
    padding: 0;
    width: 1200px;
    height: 649px;
    overflow: hidden;
    background: var(--paper);
  }
  .wrap {
    position: relative;
    width: 1200px;
    height: 649px;
    overflow: hidden;
    background: var(--paper);
  }
  .wrap-art {
    position: absolute;
    inset: 0;
    width: 1200px;
    height: 649px;
  }
  .brand {
    position: absolute;
    left: 340px;
    top: 316px;
    width: 600px;
    color: var(--ink);
    text-align: center;
  }
  .phone {
    margin: 0;
    font-family: "Roboto", sans-serif;
    font-size: 54px;
    line-height: 1;
    letter-spacing: 1px;
  }
  .name-row {
    display: flex;
    align-items: center;
    justify-content: center;
    gap: 14px;
    margin-top: 18px;
  }
  .name-mark {
    width: 30px;
    height: 30px;
    border-radius: 50%;
    background: var(--ink);
    flex: none;
  }
  .name {
    margin: 0;
    font-family: "League Spartan", sans-serif;
    font-weight: 600;
    font-size: 40px;
    line-height: 1;
  }
  .tagline {
    margin: 12px 0 0;
    font-family: "Josefin Sans", sans-serif;
    font-size: 32px;
    letter-spacing: 4px;
    line-height: 1;
  }
  .site, .email {
    margin: 14px 0 0;
    font-family: "Roboto", sans-serif;
    font-size: 20px;
    letter-spacing: 1.5px;
    line-height: 1;
  }
  .email { margin-top: 8px; }
  .categories {
    position: absolute;
    right: 20px;
    top: 616px;
    margin: 0;
    padding: 0;
    list-style: none;
    display: flex;
    gap: 8px;
    font-family: "Roboto", sans-serif;
    font-weight: 500;
    font-size: 15px;
    line-height: 1;
    letter-spacing: 0.5px;
    color: var(--paper);
  }
  .categories li + li::before {
    content: "•";
    margin-right: 8px;
    color: var(--band);
  }
</style>
</head>
<body>
<main class="wrap">
  <svg class="wrap-art" viewBox="0 0 1200 649" xmlns="http://www.w3.org/2000/svg">
    <defs>
      <linearGradient id="cone-tone" x1="0" y1="0" x2="1" y2="1">
        <stop offset="0" stop-color="#e2bd84"/>
        <stop offset="1" stop-color="#b57f45"/>
      </linearGradient>
      <linearGradient id="sprinkle-tone" x1="0" y1="0" x2="1" y2="1">
        <stop offset="0" stop-color="#f4c6d4"/>
        <stop offset="0.5" stop-color="#f2e2a6"/>
        <stop offset="1" stop-color="#b7dbe8"/>
      </linearGradient>
      <linearGradient id="ice-tone" x1="0" y1="0" x2="1" y2="1">
        <stop offset="0" stop-color="#f6df6a"/>
        <stop offset="0.55" stop-color="#f08a3a"/>
        <stop offset="1" stop-color="#d8494a"/>
      </linearGradient>
      <linearGradient id="topping-tone" x1="0" y1="0" x2="1" y2="1">
        <stop offset="0" stop-color="#7a4a34"/>
        <stop offset="0.6" stop-color="#3d2820"/>
        <stop offset="1" stop-color="#8a6fb0"/>
      </linearGradient>
    </defs>

    <polygon class="band" points="0,228 1200,8 1200,112 280,355 0,440" fill="var(--band)"/>
    <polygon class="slate-panel" points="430,649 1030,562 1200,290 1200,649" fill="var(--slate)"/>
    <polyline class="stripe" points="0,632 1018,534 1200,218" fill="none" stroke="var(--stripe)" stroke-width="14"/>

    <g class="product-tile" role="img" aria-label="Photo of a waffle cone">
      <polygon points="13,275 198,82 253,216 62,410" fill="url(#cone-tone)" stroke="var(--frame)" stroke-width="6" stroke-linejoin="round"/>
    </g>
    <g class="product-tile" role="img" aria-label="Photo of rainbow sprinkles">
      <polygon points="269,222 503,70 525,216 286,351" fill="url(#sprinkle-tone)" stroke="var(--frame)" stroke-width="6" stroke-linejoin="round"/>
    </g>
    <g class="product-tile" role="img" aria-label="Photo of water ice cups with soft serve tops">
      <polygon points="552,129 808,18 808,164 563,263" fill="url(#ice-tone)" stroke="var(--frame)" stroke-width="6" stroke-linejoin="round"/>
    </g>
    <g class="product-tile" role="img" aria-label="Photo of jars of toppings with spoons">
      <polygon points="852,14 1130,14 1108,140 841,187" fill="url(#topping-tone)" stroke="var(--frame)" stroke-width="6" stroke-linejoin="round"/>
    </g>
  </svg>

  <section class="brand">
    <p class="phone">856-217-6094</p>
    <div class="name-row">
      <span class="name-mark"></span>
      <h1 class="name">Frost Harbor Supply Inc.</h1>
    </div>
    <p class="tagline">Wholesale Distributor</p>
    <p class="site">www.frostharborsupplyinc.example</p>
    <p class="email">sales@frostharborsupplyinc.example</p>
  </section>

  <ul class="categories">
    <li>Ice Cream</li>
    <li>Mixes</li>
    <li>Syrups/Bases</li>
    <li>Toppings</li>
    <li>Cones</li>
    <li>Water Ice</li>
  </ul>
</main>
</body>
</html>
```